MORLO's Coffee Liqueur Shot Arabica

Need a lable for a 500ml bottle of homemade Coffee liqueur.
Name:
MORLO's
Coffee
Shot

Shape: Round, 80mm
Color of the lable should be black and letters in black.
Letters MORLO's min 12mm hight.
Color of the liqueur is dark brown.
Add: 500ml
Add: 38% vol.
Should have a bean on the lable.
Maybe some bullet words on the bottom...
Prefered design see Pic1a with bottle.

Target Market(s)

People that enjoy coffee in shots, in coctails, with ice or on top of icecream or any other dessert

Font styles to use
Serif

Colors

Designer to choose colors to be used in the design.

Requirements
Must have
• See Pic 1a
Nice to have
• See Pic1a (bottle)
Should not have
• Different colors

```html
<!DOCTYPE html>
<html lang="en">
<head>
<meta charset="utf-8">
<title>MORLO's Coffee Shot – Label</title>
<link rel="stylesheet" href="https://fonts.googleapis.com/css2?family=Abril+Fatface&family=Londrina+Solid:wght@900&family=Della+Respira&display=swap">
<style>
  :root {
    --ink: #000000;
    --paper: #ffffff;
    --pattern-dark: #111111;
    --pattern-mid: #3a3a3a;
  }
  html, body {
    margin: 0;
    padding: 0;
    width: 1200px;
    height: 1200px;
    overflow: hidden;
    background: var(--paper);
  }
  .label {
    display: block;
    width: 1200px;
    height: 1200px;
  }
  .brand-name {
    font-family: "Abril Fatface", Georgia, serif;
    font-size: 128px;
    letter-spacing: 6px;
    fill: var(--ink);
  }
  .product-word {
    font-family: "Londrina Solid", "Arial Black", sans-serif;
    font-weight: 900;
    fill: var(--ink);
  }
  .product-coffee { font-size: 128px; letter-spacing: 2px; }
  .product-shot { font-size: 122px; letter-spacing: 2px; }
  .spec-text {
    font-family: "Della Respira", Georgia, serif;
    font-size: 27px;
    fill: var(--ink);
    letter-spacing: 1px;
  }
  .variety-text {
    font-family: "Della Respira", Georgia, serif;
    font-size: 40px;
    fill: var(--paper);
    letter-spacing: 1.5px;
  }
  .rule { stroke: var(--ink); fill: none; }
</style>
</head>
<body>
<svg class="label" viewBox="0 0 945 945" xmlns="http://www.w3.org/2000/svg">
  <defs>
    <linearGradient id="pattern-tone" x1="0" y1="0" x2="0" y2="1">
      <stop offset="0" stop-color="var(--pattern-mid)"/>
      <stop offset="1" stop-color="var(--pattern-dark)"/>
    </linearGradient>
    <path id="brand-arc" d="M 142 472 A 330 330 0 0 1 802 472"/>
    <clipPath id="upper-half">
      <rect x="0" y="0" width="945" height="432"/>
    </clipPath>
  </defs>

  <!-- outer frame -->
  <circle class="rule" cx="472.5" cy="472.5" r="466" stroke-width="8"/>

  <!-- inner frame (upper part) -->
  <circle class="rule" cx="472.5" cy="480" r="297" stroke-width="8" clip-path="url(#upper-half)"/>

  <!-- side band -->
  <line class="rule" x1="12" y1="432" x2="183" y2="432" stroke-width="6"/>
  <line class="rule" x1="12" y1="522" x2="183" y2="522" stroke-width="6"/>
  <line class="rule" x1="762" y1="432" x2="933" y2="432" stroke-width="6"/>
  <line class="rule" x1="762" y1="522" x2="933" y2="522" stroke-width="6"/>

  <text class="spec-text" x="20" y="488">38% VOL.</text>
  <text class="spec-text" x="925" y="488" text-anchor="end">500 ML</text>

  <!-- brand name on arc -->
  <text class="brand-name">
    <textPath href="#brand-arc" startOffset="50%" text-anchor="middle">MORLO's</textPath>
  </text>

  <!-- product name -->
  <text class="product-word product-coffee" x="472.5" y="378" text-anchor="middle">COFFEE</text>
  <line class="rule" x1="248" y1="482" x2="318" y2="482" stroke-width="9"/>
  <line class="rule" x1="627" y1="482" x2="697" y2="482" stroke-width="9"/>
  <text class="product-word product-shot" x="472.5" y="528" text-anchor="middle">SHOT</text>

  <!-- bottom bean-and-leaf decoration -->
  <path role="img" aria-label="Decorative border of coffee leaves and beans along the lower rim"
        fill="url(#pattern-tone)"
        d="M 16 535 A 460 460 0 0 0 929 535 L 790 535 A 320 320 0 0 1 155 535 Z"/>

  <!-- variety pill -->
  <rect x="268" y="578" width="408" height="74" rx="37" fill="var(--ink)"/>
  <text class="variety-text" x="472.5" y="628" text-anchor="middle">Arabica Intenciv</text>

  <!-- coffee bean -->
  <ellipse role="img" aria-label="Large coffee bean" cx="472.5" cy="772" rx="64" ry="92"
           transform="rotate(18 472.5 772)" fill="var(--ink)" stroke="var(--paper)" stroke-width="8"/>
</svg>
</body>
</html>
```